Medical Clinic Website - New Private Clinic

We have a basic design for a website. Would like it developed in WORDPRESS. the attached JPG shows the page basic design.

Colours and overall design to be similar

MUST BE WORD PRESS and must allow our company to edit at later date. Images must be licenced for use.

The text to be included is:

Medical or GP clinic patients

Medical

1 page

• WORDPRESS and use the attached jpg as a design guide.
• Must be able to allow me to insert link to "slot lantern" in the top LEFT CORNER. a button or similar. The slot lantern designers will help us with this, but it must have the space

```html
<!DOCTYPE html>
<html lang="en">
<head>
<meta charset="utf-8">
<title>Harbour Lane GP</title>
<link href="https://fonts.googleapis.com/css2?family=Jura:wght@500;600&family=Open+Sans:wght@400;600&family=Roboto:wght@400;500&display=swap" rel="stylesheet">
<style>
:root{
  --page:#f6f6f7;
  --white:#ffffff;
  --blue:#2c4fa3;
  --blue-deep:#1f3c96;
  --green:#4e8f2b;
  --green-dark:#3a7421;
  --ink:#333333;
  --muted:#7a7a7a;
  --line:#dcdcdc;
  --footer:#e9e9ea;
}
*{margin:0;padding:0;box-sizing:border-box}
html,body{width:968px;height:1200px;overflow:hidden;background:var(--page)}
body{position:relative;font-family:"Open Sans",Arial,sans-serif;color:var(--ink)}
.abs{position:absolute}

/* header */
.brand{left:106px;top:52px;display:flex;align-items:center;gap:8px;font-family:"Open Sans",sans-serif;font-weight:600;font-size:21px;color:var(--blue)}
.brand-mark{width:14px;height:14px;background:var(--green)}
.booking-label{right:106px;top:27px;font-family:"Roboto",sans-serif;font-size:10px;color:#333}
.booking-line{right:106px;top:43px;font-family:"Roboto",sans-serif;font-size:13px;font-weight:500;color:var(--blue-deep);display:flex;align-items:center;gap:6px}
.booking-line .sep{margin:0 8px;color:var(--blue-deep)}
.main-nav{right:106px;top:91px;display:flex;gap:29px;font-family:"Roboto",sans-serif;font-size:12.5px;color:#333}
.main-nav .current{color:var(--green)}

/* hero */
.hero{left:0;top:128px;width:968px;height:368px;
  background:
   radial-gradient(ellipse 180px 120px at 820px 190px, rgba(70,160,180,.35), transparent 70%),
   radial-gradient(ellipse 220px 140px at 90px 160px, rgba(120,190,220,.45), transparent 70%),
   radial-gradient(ellipse 160px 80px at 760px 300px, rgba(220,190,150,.4), transparent 70%),
   linear-gradient(180deg,#e7eef2 0%,#dbe6ec 55%,#e9e4dc 100%)}
.hero-arrow{top:176px}
.hero-box{left:222px;top:62px;width:524px;height:225px;background:rgba(255,255,255,.72);border:1px solid rgba(255,255,255,.9);border-radius:2px;text-align:center}
.hero-kicker{margin-top:18px;font-size:16px;color:#444}
.hero-title{font-family:"Jura",sans-serif;font-weight:600;font-size:26px;line-height:38px;letter-spacing:-.3px}
.hero-title.blue{color:var(--blue);margin-top:3px}
.hero-title.green{color:var(--green-dark)}
.hero-copy{margin-top:6px;font-size:16px;line-height:22px;color:#111}
.hero-button{left:406px;top:266px;width:155px;height:39px;background:linear-gradient(180deg,#2d5cc4,#1d3d9a);color:#fff;font-size:12.5px;font-weight:600;display:flex;align-items:center;justify-content:center;border-radius:2px}

/* services */
.service{top:520px;width:239px;height:322px;background:var(--white)}
.service-photo{position:absolute;left:0;width:239px;height:161px}
.notch{position:absolute;left:96px;width:48px;height:24px;background:var(--white)}
.notch.up{border-radius:24px 24px 0 0}
.notch.down{border-radius:0 0 24px 24px}
.service-text{position:absolute;left:0;width:239px;text-align:center;padding:0 16px}
.service-title{font-family:"Jura",sans-serif;font-weight:600;font-size:15.5px;line-height:19px;color:var(--green)}
.service-body{margin-top:13px;font-size:7.3px;line-height:13px;color:#555}
.service-more{display:inline-block;margin-top:10px;font-size:9px;color:var(--blue);text-decoration:underline}

/* news */
.divider{left:106px;top:875px;width:755px;height:1px;background:var(--line)}
.news-heading{left:106px;top:902px;font-family:"Jura",sans-serif;font-weight:600;font-size:20px;color:var(--blue)}
.view-all{right:106px;top:910px;font-size:7.5px;color:#222;display:flex;align-items:center;gap:4px}
.news-card{top:938px;width:175px;height:142px;background:var(--white);box-shadow:1px 1px 2px rgba(0,0,0,.14);padding:27px 17px 0}
.news-date{font-size:10.5px;color:#333}
.news-body{margin-top:7px;font-size:8.6px;line-height:14px;color:var(--muted)}
.news-more{margin-top:17px;font-size:7.5px;color:#222;display:flex;align-items:center;gap:4px}

/* footer */
.site-footer{left:0;top:1122px;width:968px;height:78px;background:var(--footer)}
.footer-nav{left:106px;top:24px;font-size:8.2px;color:#333;display:flex;gap:7px}
.copyright{left:106px;top:45px;font-size:8.2px;color:#333}
.notice{right:162px;top:20px;width:320px;text-align:right;font-size:7px;line-height:12px;color:var(--muted)}
.icon-dot{top:29px;width:20px;height:20px;border-radius:50%}
</style>
</head>
<body>

<header>
  <div class="abs brand"><span class="brand-mark"></span>Harbour Lane GP</div>
  <div class="abs booking-label">To make a Booking :</div>
  <div class="abs booking-line">
    <svg width="9" height="7" viewBox="0 0 9 7"><rect width="9" height="7" fill="#1f3c96"/><path d="M0 0l4.5 3.5L9 0" stroke="#fff" fill="none" stroke-width="1"/></svg>
    reception@harbourlanegp.example
    <span class="sep">|</span>
    <svg width="6" height="9" viewBox="0 0 6 9"><rect x=".5" y=".5" width="5" height="8" rx="1" stroke="#1f3c96" fill="none"/></svg>
    6100 2400
  </div>
  <nav class="abs main-nav">
    <span class="current">Home</span><span>About Us</span><span>Services</span><span>News</span><span>Contact Us</span>
  </nav>
</header>

<section class="abs hero" role="img" aria-label="Softly blurred photo of a bright clinic waiting room">
  <svg class="abs hero-arrow" style="left:19px" width="12" height="20" viewBox="0 0 12 20"><path d="M10 2L2 10l8 8" stroke="#777" stroke-width="2" fill="none"/></svg>
  <svg class="abs hero-arrow" style="left:937px" width="12" height="20" viewBox="0 0 12 20"><path d="M2 2l8 8-8 8" stroke="#777" stroke-width="2" fill="none"/></svg>
  <div class="abs hero-box">
    <p class="hero-kicker">Unable to get a</p>
    <h1 class="hero-title blue">DOCTOR’S APPOINTMENT</h1>
    <h2 class="hero-title green">WE ARE HAPPY TO HELP</h2>
    <p class="hero-copy">Located in west riverside, We take appointments and walk in patients.<br>New patients welcome. All basic and urgent medical care<br>(Non life threatening)</p>
  </div>
  <div class="abs hero-button">GET STARTED NOW</div>
</section>

<section>
  <article class="abs service" style="left:106px">
    <div class="service-photo" style="top:0;background:linear-gradient(160deg,#dfeaf5,#8fb3dc 60%,#2f62b8)" role="img" aria-label="Photo of a stethoscope on a desk with clinicians working behind"></div>
    <div class="notch up" style="top:137px"></div>
    <div class="service-text" style="top:183px">
      <h3 class="service-title">GENERAL MEDICAL<br>CONDITIONS</h3>
      <p class="service-body">Fusce mattis risus leo, in luctus leo iaculis et. Cras mattis malesuada dolor mollis faucibus. Curabitur at consequat diam sed ante venenatis, eget pharetra diam varius. Duis nec lacus non tortor gravida.</p>
      <span class="service-more">MORE</span>
    </div>
  </article>

  <article class="abs service" style="left:365px">
    <div class="service-text" style="top:25px">
      <h3 class="service-title">UNDERTAKE A RANGE OF<br>DIAGNOSTIC SERVICES</h3>
      <p class="service-body">Fusce mattis risus leo, in luctus leo iaculis et. Cras mattis malesuada dolor mollis faucibus. Curabitur at consequat diam sed ante venenatis, eget pharetra diam varius. Duis nec lacus non tortor gravida.</p>
      <span class="service-more">MORE</span>
    </div>
    <div class="service-photo" style="top:161px;background:linear-gradient(150deg,#c9d8ec,#5f88c8 55%,#2c58a8)" role="img" aria-label="Photo of gloved hands using a laboratory microscope"></div>
    <div class="notch down" style="top:161px"></div>
  </article>

  <article class="abs service" style="left:622px">
    <div class="service-photo" style="top:0;background:linear-gradient(90deg,#eef0f2,#d9dde0 45%,#c94a45 60%,#e6e8ea)" role="img" aria-label="Photo of a physiotherapist treating a patient's shoulder"></div>
    <div class="notch up" style="top:137px"></div>
    <div class="service-text" style="top:183px">
      <h3 class="service-title">PHYSIOTHERAPY<br>SERVICE</h3>
      <p class="service-body">Fusce mattis risus leo, in luctus leo iaculis et. Cras mattis malesuada dolor mollis faucibus. Curabitur at consequat diam sed ante venenatis, eget pharetra diam varius. Duis nec lacus non tortor gravida.</p>
      <span class="service-more">MORE</span>
    </div>
  </article>
</section>

<section>
  <div class="abs divider"></div>
  <h2 class="abs news-heading">LATEST NEWS</h2>
  <div class="abs view-all">VIEW ALL <svg width="7" height="7" viewBox="0 0 8 8"><circle cx="4" cy="4" r="4" fill="#111"/><path d="M3 2l2 2-2 2" stroke="#fff" fill="none" stroke-width="1.2"/></svg></div>

  <article class="abs news-card" style="left:106px">
    <p class="news-date">8 April, 2017</p>
    <p class="news-body">Mauris et venenatis tortor, ac viverra purus. Vivamus pulvi nar dignissim arcu et aliquet.</p>
    <p class="news-more">MORE <svg width="7" height="7" viewBox="0 0 8 8"><circle cx="4" cy="4" r="4" fill="#111"/><path d="M3 2l2 2-2 2" stroke="#fff" fill="none" stroke-width="1.2"/></svg></p>
  </article>
  <article class="abs news-card" style="left:299px">
    <p class="news-date">8 April, 2017</p>
    <p class="news-body">Mauris et venenatis tortor, ac viverra purus. Vivamus pulvi nar dignissim arcu et aliquet.</p>
    <p class="news-more">MORE <svg width="7" height="7" viewBox="0 0 8 8"><circle cx="4" cy="4" r="4" fill="#111"/><path d="M3 2l2 2-2 2" stroke="#fff" fill="none" stroke-width="1.2"/></svg></p>
  </article>
  <article class="abs news-card" style="left:492px">
    <p class="news-date">8 April, 2017</p>
    <p class="news-body">Mauris et venenatis tortor, ac viverra purus. Vivamus pulvi nar dignissim arcu et aliquet.</p>
    <p class="news-more">MORE <svg width="7" height="7" viewBox="0 0 8 8"><circle cx="4" cy="4" r="4" fill="#111"/><path d="M3 2l2 2-2 2" stroke="#fff" fill="none" stroke-width="1.2"/></svg></p>
  </article>
  <article class="abs news-card" style="left:686px">
    <p class="news-date">8 April, 2017</p>
    <p class="news-body">Mauris et venenatis tortor, ac viverra purus. Vivamus pulvi nar dignissim arcu et aliquet.</p>
    <p class="news-more">MORE <svg width="7" height="7" viewBox="0 0 8 8"><circle cx="4" cy="4" r="4" fill="#111"/><path d="M3 2l2 2-2 2" stroke="#fff" fill="none" stroke-width="1.2"/></svg></p>
  </article>
</section>

<footer class="abs site-footer">
  <nav class="abs footer-nav"><span>Home</span><span>|</span><span>About Us</span><span>|</span><span>Services</span><span>|</span><span>News</span><span>|</span><span>Contact Us</span></nav>
  <p class="abs copyright">Copyright © 2017 &nbsp;Company name. &nbsp;All rights reserved.</p>
  <p class="abs notice">If you are experiencing any chest pain difficulty with breathing or any acute symptoms associated with the heart lumos or the brain. Please go to your nearest hospital or call the City Ambulance on immediately. Do not wait in the wasing room</p>
  <div class="abs icon-dot" style="left:814px;background:var(--blue-deep)"></div>
  <svg class="abs icon-dot" style="left:840px" width="20" height="20" viewBox="0 0 20 20"><circle cx="10" cy="10" r="10" fill="#4e9a3a"/><rect x="5" y="6.5" width="10" height="7" rx="1" fill="#fff"/><path d="M5.5 7l4.5 3.5L14.5 7" stroke="#4e9a3a" fill="none" stroke-width="1"/></svg>
</footer>

</body>
</html>
```